Dietary supplement package design

We need a design for a range of dietary supplements mentioned below. The colors can be derived from the attached company logo and the package is a plastic bottle for medicines use (attached is a sample). All products will have the same package design and color with a permissible slight change to product name and associated picture/artwork (if any). Please avoid using pictures of humans or animals. We expect to see a label with three panels:
1. Left panel containing instructions, warnings and other information.
2. Front panel containing products name and its unique look
3. Right panel containing nutrient/ingredient information table and address.
The label will dual language (Arabic/English) and we have no issue to use special colors, i.e. UV, gold or silver.
Products names are:
1. Ginkgo biloba
2. Slimming formula
3. Fat Absorber
4. Glutathione
5. Royal Jelly
6. Vitamin D
Reason: Allow designers to provide more suggestions
Target Market(s)
Consumers and health care professionals
Industry/Entity Type
Healthcare
Look and feel

```html
<!DOCTYPE html>
<html lang="en">
<head>
<meta charset="utf-8">
<title>Vantora Supplement Label Range</title>
<link rel="stylesheet" href="https://fonts.googleapis.com/css2?family=Cinzel:wght@600&display=swap">
<style>
  :root {
    --blue: #29abe2;
    --orange: #fbb03b;
    --green: #22a33a;
    --label-bg: #f2f2f2;
    --page-bg: #ffffff;
    --white: #ffffff;
  }
  * { margin: 0; padding: 0; box-sizing: border-box; }
  html, body { width: 1200px; height: 900px; overflow: hidden; background: var(--page-bg); }
  body { position: relative; font-family: "Cinzel", "Times New Roman", serif; }

  /* shared label faces */
  .label {
    position: absolute;
    background: var(--label-bg);
    box-shadow: 2px 3px 6px rgba(0,0,0,0.28);
  }
  .face {
    position: absolute;
    top: 0; bottom: 0;
    left: 50%;
    transform: translateX(-50%);
    overflow: hidden;
  }
  .corner { position: absolute; }
  .corner--tl { top: 0; left: 0; background: var(--blue); clip-path: polygon(0 0, 100% 0, 0 100%); }
  .corner--tr { top: 0; right: 0; background: var(--orange); clip-path: polygon(0 0, 100% 0, 100% 100%); }
  .corner--bl { bottom: 0; left: 0; background: var(--green); clip-path: polygon(0 0, 0 100%, 100% 100%); }
  .corner--br { bottom: 0; right: 0; background: var(--blue); clip-path: polygon(100% 0, 100% 100%, 0 100%); }

  .brand {
    position: absolute;
    left: 0; right: 0;
    display: flex; align-items: center; justify-content: center;
    color: var(--blue);
    font-weight: 600;
  }
  .brand__mark { background: var(--blue); }

  .band { position: absolute; left: 0; right: 0; }
  .band__name {
    display: block;
    border-top: 1px solid var(--white);
    border-bottom: 1px solid var(--white);
    color: var(--white);
    text-align: center;
    font-weight: 600;
    white-space: nowrap;
  }
  .band--green { background: var(--green); }
  .band--blue { background: var(--blue); }
  .band--orange { background: var(--orange); }

  /* hero label */
  .label--hero { left: 74px; top: 372px; width: 358px; height: 368px; }
  .label--hero .face { width: 358px; }
  .label--hero .corner { width: 88px; height: 88px; }
  .label--hero .brand { top: 58px; font-size: 26px; gap: 10px; }
  .label--hero .brand__mark { width: 22px; height: 22px; }
  .label--hero .band { top: 164px; padding: 4px 0; }
  .label--hero .band__name { font-size: 31px; line-height: 40px; border-width: 2px; }

  /* range labels */
  .label--mini { width: 308px; height: 149px; }
  .label--mini .face { width: 144px; border-radius: 12px; }
  .label--mini .corner { width: 42px; height: 42px; }
  .label--mini .brand { top: 14px; font-size: 10px; gap: 4px; }
  .label--mini .brand__mark { width: 9px; height: 9px; }
  .label--mini .band { top: 65px; padding: 2px 0; }
  .label--mini .band__name { font-size: 12px; line-height: 16px; }

  .col-1 { left: 522px; }
  .col-2 { left: 864px; }
  .row-1 { top: 204px; }
  .row-2 { top: 394px; }
  .row-3 { top: 584px; }
</style>
</head>
<body>

<section class="label label--hero">
  <div class="face">
    <span class="corner corner--tl"></span><span class="corner corner--tr"></span>
    <span class="corner corner--bl"></span><span class="corner corner--br"></span>
    <div class="brand"><span class="brand__mark"></span>Vantora</div>
    <div class="band band--green"><span class="band__name">Ginkgo Biloba</span></div>
  </div>
</section>

<section class="label label--mini col-1 row-1">
  <div class="face">
    <span class="corner corner--tl"></span><span class="corner corner--tr"></span>
    <span class="corner corner--bl"></span><span class="corner corner--br"></span>
    <div class="brand"><span class="brand__mark"></span>Vantora</div>
    <div class="band band--green"><span class="band__name">Ginkgo Biloba</span></div>
  </div>
</section>

<section class="label label--mini col-2 row-1">
  <div class="face">
    <span class="corner corner--tl"></span><span class="corner corner--tr"></span>
    <span class="corner corner--bl"></span><span class="corner corner--br"></span>
    <div class="brand"><span class="brand__mark"></span>Vantora</div>
    <div class="band band--blue"><span class="band__name">Glutathione</span></div>
  </div>
</section>

<section class="label label--mini col-1 row-2">
  <div class="face">
    <span class="corner corner--tl"></span><span class="corner corner--tr"></span>
    <span class="corner corner--bl"></span><span class="corner corner--br"></span>
    <div class="brand"><span class="brand__mark"></span>Vantora</div>
    <div class="band band--orange"><span class="band__name">Slimming Formula</span></div>
  </div>
</section>

<section class="label label--mini col-2 row-2">
  <div class="face">
    <span class="corner corner--tl"></span><span class="corner corner--tr"></span>
    <span class="corner corner--bl"></span><span class="corner corner--br"></span>
    <div class="brand"><span class="brand__mark"></span>Vantora</div>
    <div class="band band--orange"><span class="band__name">Royal Jelly</span></div>
  </div>
</section>

<section class="label label--mini col-1 row-3">
  <div class="face">
    <span class="corner corner--tl"></span><span class="corner corner--tr"></span>
    <span class="corner corner--bl"></span><span class="corner corner--br"></span>
    <div class="brand"><span class="brand__mark"></span>Vantora</div>
    <div class="band band--blue"><span class="band__name">Fat Absorber</span></div>
  </div>
</section>

<section class="label label--mini col-2 row-3">
  <div class="face">
    <span class="corner corner--tl"></span><span class="corner corner--tr"></span>
    <span class="corner corner--bl"></span><span class="corner corner--br"></span>
    <div class="brand"><span class="brand__mark"></span>Vantora</div>
    <div class="band band--green"><span class="band__name">Vitamin D</span></div>
  </div>
</section>

</body>
</html>
```